Fontaneau Bayou Grillhouse (Owners Card)

Need a classy, but modern business card. I have included a promotional card for the steakhouse. I need one for myself (the owner) that is more professional.

Target Market(s)

General Public

Industry/Entity Type

Food service

Contact Information for Business Card

Name, business address, phone number, email, logo

Font styles to use
Serif
Sans Serif
Decorative
Script

Requirements
Must have
• My name (Darvin Okafor), business address (627 Harlow Avenue), phone number (520) 394-2751, email (Dokaforzp4@mailbrook.net. On the back of the card: Psalms 27 1 The LORD is my light and my salvation— whom shall I fear? The LORD is the stronghold of my life— of whom shall I be afraid? 2 When the wicked advance against me to devour me, it is my enemies and my foes who will stumble and fall. 3 Though an army besiege me, my heart will not fear; though war break out against me, even then I will be confident.
Nice to have
• Something that’s bold, but modern and professional.

```html
<!DOCTYPE html>
<html lang="en">
<head>
<meta charset="utf-8">
<title>Fontaneau Bayou Grillhouse – Owner Business Card</title>
<link rel="stylesheet" href="https://fonts.googleapis.com/css2?family=Libre+Baskerville:wght@400;700&display=swap">
<style>
  :root {
    --page-bg: #ececec;
    --card-bg: #000000;
    --text-light: #ffffff;
    --name-orange: #f08a24;
    --icon-yellow: #e4d63c;
    --brand-gold: #e9a93a;
  }
  * { box-sizing: border-box; margin: 0; padding: 0; }
  html, body {
    width: 1200px; height: 1200px; overflow: hidden;
    background: var(--page-bg);
  }
  body { position: relative; font-family: "Libre Baskerville", "Times New Roman", serif; }

  .card {
    position: absolute; left: 160px; width: 877px; height: 512px;
    background: var(--card-bg); color: var(--text-light);
  }
  .card--front { top: 67px; }
  .card--back { top: 617px; }

  /* Front */
  .brand {
    position: absolute; left: 60px; top: 66px; width: 366px;
    display: flex; flex-direction: column; align-items: center; gap: 18px;
  }
  .brand-dot {
    width: 70px; height: 70px; border-radius: 50%;
    background: var(--brand-gold);
  }
  .brand-name {
    color: var(--brand-gold); font-weight: 700; font-size: 30px;
    line-height: 1.25; text-align: center; letter-spacing: 0.5px;
  }
  .divider {
    position: absolute; left: 40px; top: 357px; width: 325px; height: 3px;
    background: var(--text-light);
  }
  .owner-name {
    position: absolute; right: 69px; top: 288px;
    color: var(--name-orange); font-weight: 700; font-size: 35px;
    letter-spacing: 0.5px; white-space: nowrap;
  }
  .contact-list {
    position: absolute; right: 66px; top: 367px; list-style: none;
  }
  .contact-item {
    display: flex; justify-content: flex-end; align-items: center;
    height: 34px; font-size: 20px; gap: 16px;
  }
  .contact-icon { width: 18px; height: 18px; flex: none; }
  .contact-icon path, .contact-icon rect, .contact-icon circle { fill: var(--icon-yellow); }

  /* Back */
  .verse {
    position: absolute; left: 0; right: 0; top: 92px;
    text-align: center; font-size: 20px; line-height: 34px;
  }
  .verse-title { margin-bottom: 34px; }
  .verse-stanza { margin-bottom: 34px; }
</style>
</head>
<body>
  <section class="card card--front" aria-label="Business card front">
    <div class="brand">
      <span class="brand-dot"></span>
      <span class="brand-name">Fontaneau Bayou<br>Grillhouse</span>
    </div>
    <div class="divider"></div>
    <h1 class="owner-name">DARVIN OKAFOR</h1>
    <ul class="contact-list">
      <li class="contact-item">
        <span>(520) 394-2751</span>
        <svg class="contact-icon" viewBox="0 0 24 24" aria-hidden="true"><path d="M6.6 10.8a15.1 15.1 0 0 0 6.6 6.6l2.2-2.2a1 1 0 0 1 1-.25 11.4 11.4 0 0 0 3.6.6 1 1 0 0 1 1 1V20a1 1 0 0 1-1 1A17 17 0 0 1 3 4a1 1 0 0 1 1-1h3.5a1 1 0 0 1 1 1 11.4 11.4 0 0 0 .6 3.6 1 1 0 0 1-.25 1z"/></svg>
      </li>
      <li class="contact-item">
        <span>Dokaforzp4@mailbrook.net</span>
        <svg class="contact-icon" viewBox="0 0 24 24" aria-hidden="true"><path d="M7 1h10a2 2 0 0 1 2 2v18a2 2 0 0 1-2 2H7a2 2 0 0 1-2-2V3a2 2 0 0 1 2-2zm0 3v14h10V4zm5 15.5a1 1 0 1 0 0 2 1 1 0 0 0 0-2z"/></svg>
      </li>
      <li class="contact-item">
        <span>627 Harlow Avenue</span>
        <svg class="contact-icon" viewBox="0 0 24 24" aria-hidden="true"><path d="M12 1a8 8 0 0 0-8 8c0 6 8 14 8 14s8-8 8-14a8 8 0 0 0-8-8zm0 11a3 3 0 1 1 0-6 3 3 0 0 1 0 6z"/></svg>
      </li>
    </ul>
  </section>

  <section class="card card--back" aria-label="Business card back">
    <div class="verse">
      <p class="verse-title">Psalms 27</p>
      <p class="verse-stanza">The LORD is my light and my salvation—&nbsp; whom shall I fear? The<br>LORD is the stronghold of my life—&nbsp; of whom shall I be afraid?</p>
      <p class="verse-stanza">When the wicked advance against me to devour me, it is my enemies<br>and my foes who will stumble and fall.</p>
      <p class="verse-stanza">Though an army besiege me, my heart will not fear; though war<br>break out against me, even then I will be confident.</p>
    </div>
  </section>
</body>
</html>
```